Need Business cards

Im a new realtor and already have a logo. I would like to purchase a Business card design that catches customer's attention, its creative, and modern.

Marisol Quintero
Realtor ®
(555) 318 4027
marisolqtrhomes@brindlemail.com

Target Market(s)

investors, buyers and seller, property management

Industry/Entity Type

real estate,

Contact Information for Business Card

Marisol Quintero

Requirements
Must have
• BOTH LOGOS, WOULD LIKE TO SEE WITH DIFFERENT OPTIONS WITH EITHER PICTURE

```html
<!DOCTYPE html>
<html lang="en">
<head>
<meta charset="utf-8">
<title>Marisol Quintero – Realtor Business Cards</title>
<link rel="stylesheet" href="https://fonts.googleapis.com/css2?family=Montserrat:wght@500;600&family=Rubik:wght@400;500;600&display=swap">
<style>
  :root {
    --backdrop: #2a2a2a;
    --card-black: #1b1b1b;
    --card-black-deep: #161616;
    --mark-grey: #3a3a3a;
    --gold: #c9a227;
    --gold-light: #e6c552;
    --paper: #f1f1f1;
    --navy: #0f1d40;
    --brand-blue: #2e7bd6;
  }
  * { margin: 0; padding: 0; box-sizing: border-box; }
  html, body { width: 1200px; height: 1138px; overflow: hidden; }
  body {
    background: var(--backdrop);
    position: relative;
    font-family: "Rubik", Arial, sans-serif;
  }

  .card {
    position: absolute;
    border-radius: 14px;
    overflow: hidden;
    box-shadow: 0 10px 24px rgba(0,0,0,0.35);
  }

  /* Front */
  .card-front {
    left: 274px; top: 186px; width: 622px; height: 378px;
    background: var(--card-black);
  }
  .front-mark {
    position: absolute;
    left: 0; right: 0; top: 162px;
    text-align: center;
    font-family: "Rubik", Arial, sans-serif;
    font-weight: 500;
    font-size: 40px;
    color: var(--mark-grey);
    letter-spacing: 0.5px;
  }

  /* Back */
  .card-back {
    left: 276px; top: 607px; width: 618px; height: 375px;
    background: var(--paper);
  }
  .card-back .panel { position: absolute; inset: 0; }

  .agent-mark {
    position: absolute;
    left: 0; width: 260px; top: 120px;
    text-align: center;
    color: var(--gold);
  }
  .agent-mark .mark-name {
    font-family: "Montserrat", Arial, sans-serif;
    font-weight: 600;
    font-size: 30px;
    line-height: 1.05;
    color: var(--gold);
  }
  .agent-mark .mark-caption {
    margin-top: 36px;
    font-family: "Montserrat", Arial, sans-serif;
    font-weight: 600;
    font-size: 15px;
    letter-spacing: 0.4px;
  }
  .agent-mark .mark-role {
    display: flex; align-items: center; justify-content: center;
    gap: 6px;
    margin-top: 2px;
    font-family: "Montserrat", Arial, sans-serif;
    font-weight: 500;
    font-size: 11px;
    letter-spacing: 0.6px;
  }
  .agent-mark .mark-role::before,
  .agent-mark .mark-role::after {
    content: ""; width: 48px; height: 1px; background: var(--gold);
  }

  .brokerage {
    position: absolute;
    right: 32px; top: 50px;
    display: flex; align-items: center; gap: 8px;
    font-family: "Rubik", Arial, sans-serif;
    font-weight: 600;
    font-size: 26px;
    color: var(--brand-blue);
    letter-spacing: 0.5px;
  }
  .brokerage .brand-square {
    width: 10px; height: 10px; background: var(--brand-blue);
  }

  .contact-block {
    position: absolute;
    right: 32px; top: 212px;
    text-align: right;
    color: var(--navy);
  }
  .agent-name { font-weight: 600; font-size: 27px; line-height: 1.1; }
  .agent-title { font-size: 14px; margin-top: 4px; }
  .agent-title sup { font-size: 8px; }

  .contact-list { list-style: none; margin-top: 32px; }
  .contact-list li {
    display: flex; align-items: center; justify-content: flex-end;
    gap: 16px;
    font-size: 15px;
    height: 26px;
  }
  .contact-list svg { width: 14px; height: 14px; fill: var(--navy); }
</style>
</head>
<body>

  <section class="card card-front" aria-label="Card front">
    <div class="front-mark">Marisol Quintero</div>
  </section>

  <section class="card card-back" aria-label="Card back">
    <svg class="panel" viewBox="0 0 618 375" preserveAspectRatio="none" aria-hidden="true">
      <defs>
        <linearGradient id="goldEdge" x1="0" y1="0" x2="0" y2="1">
          <stop offset="0" stop-color="#e6c552"/>
          <stop offset="0.5" stop-color="#b8901c"/>
          <stop offset="1" stop-color="#e0bd48"/>
        </linearGradient>
      </defs>
      <path d="M0 0 H238 Q316 190 230 375 H0 Z" fill="url(#goldEdge)"/>
      <path d="M0 0 H230 Q304 190 222 375 H0 Z" fill="#171717"/>
      <path d="M618 193 Q600 193 600 235 Q600 277 618 277 Z" fill="url(#goldEdge)"/>
    </svg>

    <div class="agent-mark">
      <div class="mark-name">Marisol<br>Quintero</div>
      <div class="mark-caption">MARISOL QUINTERO</div>
      <div class="mark-role">REALTOR</div>
    </div>

    <div class="brokerage">
      <span class="brand-square"></span>
      <span>CRESTLINE REALTY</span>
    </div>

    <div class="contact-block">
      <div class="agent-name">Marisol Quintero</div>
      <div class="agent-title">Realtor<sup>®</sup></div>
      <ul class="contact-list">
        <li>
          <span>(555) 318 4027</span>
          <svg viewBox="0 0 24 24" aria-hidden="true"><path d="M3 8c0-3 4-5 9-5s9 2 9 5v2h-5V8c-1-.6-2.3-1-4-1s-3 .4-4 1v2H3zM6 12h12l3 8H3z"/></svg>
        </li>
        <li>
          <span>marisolqtrhomes@brindlemail.com</span>
          <svg viewBox="0 0 24 24" aria-hidden="true"><path d="M2 5h20v14H2zM4 7v1l8 5 8-5V7l-8 5z"/></svg>
        </li>
      </ul>
    </div>
  </section>

</body>
</html>
```